Letterhead and envelope design

Using current logo and colours I would like to have a new design done for a stationary set to be printed.

The new files should include logo, web and email address as well as,mailing address and phone number

Rory Vantosh
Vantosh Building Inc
Box 27 Site 18 RR5
Okotoks AB
T4M 2B7
Cell : 403-555-2917
Email: rory@vantoshbuilding.example
web: vantoshbuilding.example

```html
<!DOCTYPE html>
<html lang="en">
<head>
<meta charset="utf-8">
<title>Vantosh Building Inc – Stationery Set</title>
<link href="https://fonts.googleapis.com/css2?family=Montserrat:wght@300;400;500;600&family=Arimo:wght@400;700&family=Italianno&display=swap" rel="stylesheet">
<style>
  :root {
    --navy: #062b5e;
    --orange: #e07f10;
    --stage: #ababab;
    --paper: #ffffff;
    --body-grey: #8a8a8a;
    --heading-grey: #6d6d6d;
    --ink: #3d3d3d;
  }
  * { margin: 0; padding: 0; box-sizing: border-box; }
  html, body { width: 1200px; height: 900px; overflow: hidden; }
  body { background: var(--stage); position: relative; font-family: "Montserrat", sans-serif; }

  .sheet { position: absolute; background: var(--paper); box-shadow: 1px 2px 4px rgba(0,0,0,.25); overflow: hidden; }
  .sheet svg { position: absolute; inset: 0; }

  .letterhead { left: 65px; top: 106px; width: 473px; height: 668px; }
  .envelope-front { left: 570px; top: 153px; width: 565px; height: 245px; }
  .envelope-back { left: 570px; top: 476px; width: 565px; height: 246px; }

  .wordmark { font-family: "Montserrat", sans-serif; font-weight: 600; fill: var(--navy); }
  .wordmark.on-navy { fill: var(--paper); }
  .contact { font-family: "Arimo", sans-serif; font-size: 7.6px; fill: var(--navy); }
  .contact .company { font-weight: 700; fill: var(--orange); }

  .letter-body {
    position: absolute; left: 39px; top: 218px; width: 396px;
    color: var(--body-grey); font-size: 7px; font-weight: 300; line-height: 8.8px; text-align: justify;
  }
  .letter-body .salutation { color: var(--heading-grey); font-size: 9.2px; font-weight: 500; margin-bottom: 6px; margin-left: -1px; }
  .letter-body p { margin-bottom: 8.6px; }
  .sign-off { position: absolute; left: 38px; top: 470px; color: var(--ink); }
  .sign-off .signature { font-family: "Italianno", cursive; font-size: 22px; color: var(--ink); line-height: 24px; }
  .sign-off .name { font-size: 8px; font-weight: 400; margin-top: 4px; letter-spacing: .2px; }
  .sign-off .role { font-size: 6px; font-weight: 300; color: var(--body-grey); margin-top: 1px; }
</style>
</head>
<body>

<section class="sheet letterhead">
  <svg width="473" height="668" viewBox="0 0 473 668">
    <rect class="band" x="0" y="61" width="36" height="7" fill="var(--navy)"/>
    <rect class="band" x="180" y="61" width="293" height="7" fill="var(--navy)"/>
    <rect class="rule" x="0" y="72" width="473" height="1.6" fill="var(--orange)"/>
    <rect x="36" y="58" width="144" height="18" fill="var(--paper)"/>
    <circle cx="63" cy="57" r="25.5" fill="var(--navy)"/>
    <text class="wordmark" x="96" y="57" font-size="13.5">VANTOSH</text>
    <text class="wordmark" x="96" y="70" font-size="10.5">BUILDING</text>

    <g class="contact">
      <text class="company" x="315" y="32" text-anchor="end">Vantosh Building Inc</text>
      <text x="315" y="42" text-anchor="end">Box 27 Site 18 RR5</text>
      <text x="315" y="52" text-anchor="end">Marrowdale, MB T4M 2B7</text>
    </g>
    <line x1="322.5" y1="25" x2="322.5" y2="54" stroke="var(--orange)" stroke-width=".8"/>
    <g class="icons" fill="none" stroke="var(--orange)" stroke-width=".7">
      <path d="M330.5 26.5 q-.6 2 1.5 4.5 q2.2 2 3.4 1.2 l.4-.9 -1.4-1 -.7.6 q-1.3-.8-2-2.2 l.6-.7 -1-1.4z" fill="var(--orange)" stroke="none"/>
      <rect x="330" y="37.5" width="5.6" height="4"/>
      <path d="M330 37.6 l2.8 2.2 2.8-2.2"/>
      <circle cx="332.8" cy="48.5" r="2.7"/>
      <path d="M330.1 48.5 h5.4 M332.8 45.8 q-1.6 2.7 0 5.4 q1.6-2.7 0-5.4"/>
    </g>
    <g class="contact">
      <text x="339" y="32">403-555-2917</text>
      <text x="339" y="42">rory@vantoshbuilding.example</text>
      <text x="339" y="52">vantoshbuilding.example</text>
    </g>
  </svg>

  <div class="letter-body">
    <div class="salutation">Dear Mr. Hale</div>
    <p>Lorem ipsum dolor sit amet, consectetuer adipiscing elit, sed diam nonmmy nibh euismod tincidunt ut laoreet dolore magna aliquam erat volutpat. Ut wisi enim ad minim veniam, quis nostrud exerci tationmcorper suscipit lobortis nisl ut aliquip ex ea commodo consequat. Duis autem vel eum iriure dolor in hendrerit in vulputate velit esse molestie consequat, vel illum dolore eu feugiat nulla facilisis at vero eros et accumsan et iusto odio dignissim qui blandit praesent luptatum zzril delenit augue duis dolore te feugait nulla facilisi.</p>
    <p>Nam liber tempor cum soluta nobis eleifend option congue nihil imprdiet doming id quod mazim placerat facer possim assum. Typi non habent claritatem insitam;</p>
    <p>Est usus legentis in iis qui facit eorum claritatem.</p>
    <p>Investigationes demonstraverunt lectores legere me lius quod ii legunt saepius. Claritas est etiam processus dynamicus, qui sequitur mutationem consuetudium lectorum. Mirum est notare quam littera gothica, quam nunc putamus parum claram, anteposuerit litterarum formas humanitatis per seacula quarta decima et quinta decima. Eodem modo typi, qui nunc nobis videntur parum clari, fiant sollemnes in futurum.</p>
    <p>consectetuer adipiscing elit, sed diam nonummy nibh euismod tincidunt ut laoreet dolore magna aliquam erat volutpat. Ut wisi enim ad minim veniam, quis nostrud exerci tation ullamcorper suscipit lobortis nisl ut aliquip ex ea commodo consequat. Duis autem vel eum iriure dolor in hendrerit in vulputate velit esse molestie consequat, vel illum dolore eu feugiat nulla facilisis at vero eros et accumsan et iusto odio dignissim qui blandit praesent luptatum zzril delenit augue duis dolore te feugait nulla facilisi.</p>
    <p>Nam liber tempor cum soluta nobis eleifend option congue nihil imperdiet .</p>
  </div>

  <div class="sign-off">
    <div class="signature">owen marlow</div>
    <div class="name">Owen Marlow</div>
    <div class="role">Managing Director</div>
  </div>
</section>

<section class="sheet envelope-front">
  <svg width="565" height="245" viewBox="0 0 565 245">
    <rect x="0" y="43" width="20" height="8" fill="var(--navy)"/>
    <rect x="169" y="43" width="396" height="8" fill="var(--navy)"/>
    <rect x="0" y="55" width="565" height="1.8" fill="var(--orange)"/>
    <rect x="20" y="52" width="149" height="10" fill="var(--paper)"/>
    <circle cx="48" cy="40" r="26.5" fill="var(--navy)"/>
    <text class="wordmark" x="81" y="38" font-size="14">VANTOSH</text>
    <text class="wordmark" x="81" y="52" font-size="11">BUILDING</text>
    <g class="contact" style="font-size:8px">
      <text x="83" y="71">Box 27 Site 18 RR5</text>
      <text x="83" y="81">Marrowdale, MB T4M 2B7</text>
    </g>
  </svg>
</section>

<section class="sheet envelope-back">
  <svg width="565" height="246" viewBox="0 0 565 246">
    <defs>
      <filter id="flap-shadow" x="-5%" y="-20%" width="110%" height="160%">
        <feDropShadow dx="0" dy="4" stdDeviation="3" flood-color="#000" flood-opacity=".22"/>
      </filter>
    </defs>
    <path class="flap" d="M0 0 H565 L553 52 Q549 67 531 67 H34 Q16 67 12 52 Z" fill="var(--navy)" filter="url(#flap-shadow)"/>
    <circle cx="241" cy="33.5" r="25" fill="none" stroke="var(--paper)" stroke-width="1"/>
    <text class="wordmark on-navy" x="271" y="32" font-size="12">VANTOSH</text>
    <text class="wordmark on-navy" x="271" y="45" font-size="9.5">BUILDING</text>
  </svg>
</section>

</body>
</html>
```